Marrowfield Systems Business Card

I am a managed service provider and general business technology partner for all IT services. I really enjoy design layout of https://www.pixelbazaar-demo.com/design/40627718 and would like something like this but focus graphically a little more on the constellation kind of images. I have provided my logo I want to use I own the rights to it. On the front I would like the tag line to be "Simple Solutions for Complex Connections" With the logo and attached background. The information side in the bottom left I would like "We Make IT Happen." the Logo how they did it twice I think looks great. Marrowfield Systems LLC for the Business name. My Name is Garrett Holloway M.S. Owner
Email: Garrett@Marrowfield-Sys.example
Cell: 555-214-3796

I look forward to seeing your work

Font styles to use
Serif

```html
<!DOCTYPE html>
<html lang="en">
<head>
<meta charset="utf-8">
<title>Marrowfield Systems – Business Card</title>
<link rel="stylesheet" href="https://fonts.googleapis.com/css2?family=Rubik:wght@400;500;600&family=Montserrat:wght@500;600&display=swap">
<style>
  :root {
    --navy-deep: #0c1650;
    --navy: #1a2a86;
    --blue: #2c4fc0;
    --blue-bright: #3a6ad8;
    --band-light: #4a64b4;
    --band-dark: #101a5a;
    --white: #ffffff;
    --muted: #dfe4f5;
    --rule: #b9c0dc;
    --orange: #f28a1c;
    --yellow: #ffc21a;
  }
  * { margin: 0; padding: 0; box-sizing: border-box; }
  html, body { width: 1200px; height: 686px; overflow: hidden; background: #e9ebf2; }
  .card {
    position: relative;
    width: 1200px;
    height: 686px;
    overflow: hidden;
    font-family: "Rubik", sans-serif;
    color: var(--white);
  }
  .backdrop {
    position: absolute; inset: 0;
    background:
      radial-gradient(ellipse at 70% 45%, rgba(58,106,216,0.55) 0%, rgba(58,106,216,0) 55%),
      linear-gradient(120deg, var(--navy-deep) 0%, var(--navy) 40%, var(--blue) 70%, var(--navy-deep) 100%);
  }
  .network-area {
    position: absolute; top: 0; right: 0; width: 440px; height: 600px;
    background: radial-gradient(ellipse at 65% 40%, rgba(200,215,255,0.18) 0%, rgba(200,215,255,0) 70%);
  }
  .brand {
    position: absolute; left: 80px; top: 52px;
    display: flex; align-items: center; gap: 62px;
  }
  .brand-dot {
    width: 112px; height: 112px; border-radius: 50%;
    background: var(--orange);
  }
  .brand-name {
    font-weight: 600; color: var(--white); line-height: 1.15;
    text-transform: uppercase;
  }
  .brand-name .line-main { display: block; font-size: 46px; letter-spacing: 0.5px; }
  .brand-name .line-sub { display: block; font-size: 31px; letter-spacing: 5px; margin-top: 4px; }
  .accent-bar {
    position: absolute; left: 0; top: 294px; width: 13px; height: 78px;
    background: linear-gradient(180deg, var(--orange), var(--yellow));
  }
  .person { position: absolute; left: 65px; top: 290px; }
  .person-name { font-size: 38px; font-weight: 500; letter-spacing: 0.5px; }
  .person-role { margin-top: 12px; font-size: 25px; font-weight: 400; letter-spacing: 2.5px; color: var(--muted); }
  .divider { position: absolute; left: 65px; top: 389px; width: 498px; height: 2px; background: var(--rule); }
  .contacts { position: absolute; left: 65px; top: 424px; list-style: none; }
  .contacts li { display: flex; align-items: center; height: 30px; margin-bottom: 22px; font-size: 20px; }
  .contacts .icon { width: 28px; display: flex; justify-content: center; margin-right: 19px; }
  .tagline-band {
    position: absolute; left: 0; top: 623px; width: 730px; height: 63px;
    background: linear-gradient(90deg, var(--band-light) 0%, var(--navy) 60%, var(--band-dark) 100%);
    clip-path: polygon(0 0, 688px 0, 730px 63px, 0 63px);
  }
  .tagline {
    position: absolute; left: 65px; top: 643px;
    font-family: "Montserrat", sans-serif; font-weight: 600;
    font-size: 24px; letter-spacing: 4.5px; text-transform: uppercase;
  }
  .web-band {
    position: absolute; left: 760px; top: 623px; width: 440px; height: 63px;
    background: var(--band-dark);
    clip-path: polygon(0 0, 440px 0, 440px 63px, 40px 63px);
  }
  .web-rule {
    position: absolute; left: 800px; top: 681px; width: 400px; height: 5px;
    background: linear-gradient(90deg, var(--orange), var(--yellow));
  }
  .website {
    position: absolute; left: 790px; top: 638px;
    display: flex; align-items: center; gap: 10px;
    font-family: "Montserrat", sans-serif; font-weight: 600;
    font-size: 16px; letter-spacing: 2px; text-transform: uppercase;
  }
</style>
</head>
<body>
  <div class="card">
    <div class="backdrop" role="img" aria-label="Deep blue low-poly faceted background"></div>
    <div class="network-area" role="img" aria-label="Faint white constellation network of points and lines"></div>

    <div class="brand">
      <span class="brand-dot"></span>
      <div class="brand-name">
        <span class="line-main">Marrowfield</span>
        <span class="line-sub">Systems LLC</span>
      </div>
    </div>

    <div class="accent-bar"></div>
    <div class="person">
      <h1 class="person-name">GARRETT HOLLOWAY M.S.</h1>
      <p class="person-role">OWNER</p>
    </div>
    <div class="divider"></div>

    <ul class="contacts">
      <li>
        <span class="icon">
          <svg width="26" height="18" viewBox="0 0 26 18"><rect x="1" y="1" width="24" height="16" fill="none" stroke="#fff" stroke-width="2"/><path d="M1 1 L13 10 L25 1" fill="none" stroke="#fff" stroke-width="2"/></svg>
        </span>
        Email: Garrett@Marrowfield-Sys.example
      </li>
      <li>
        <span class="icon">
          <svg width="24" height="24" viewBox="0 0 24 24"><path fill="#fff" d="M6.6 10.8c1.4 2.8 3.8 5.1 6.6 6.6l2.2-2.2c.3-.3.7-.4 1-.2 1.1.4 2.3.6 3.6.6.6 0 1 .4 1 1V20c0 .6-.4 1-1 1C10.6 21 3 13.4 3 4c0-.6.4-1 1-1h3.5c.6 0 1 .4 1 1 0 1.3.2 2.5.6 3.6.1.3 0 .7-.2 1l-2.3 2.2z"/></svg>
        </span>
        Phone: 555-214-3796
      </li>
      <li>
        <span class="icon">
          <svg width="18" height="30" viewBox="0 0 18 30"><rect x="1.5" y="1.5" width="15" height="27" rx="3" fill="none" stroke="#fff" stroke-width="2.2"/><line x1="6" y1="24" x2="12" y2="24" stroke="#fff" stroke-width="2"/></svg>
        </span>
        Cell: 555-214-3796
      </li>
    </ul>

    <div class="tagline-band"></div>
    <p class="tagline">We Make IT Happen</p>

    <div class="web-band"></div>
    <div class="web-rule"></div>
    <p class="website">
      <svg width="20" height="20" viewBox="0 0 20 20" fill="none" stroke="#fff" stroke-width="1.5"><circle cx="10" cy="10" r="8.5"/><ellipse cx="10" cy="10" rx="3.8" ry="8.5"/><line x1="1.5" y1="10" x2="18.5" y2="10"/><line x1="3" y1="5.5" x2="17" y2="5.5"/><line x1="3" y1="14.5" x2="17" y2="14.5"/></svg>
      www.marrowfield-sys.example
    </p>
  </div>
</body>
</html>
```